Car Wrap Design - Black Van

Client Name: Tom Haddley
Business: Haddley Locksmiths
Design Job: Vehicle Wrap Design
Vehicle: 2022 Dellorin Carvex L2. Note: I don’t have the actual van yet but have included images of examples of the van.
Vehicle Colour: Black
Mandatory Inclusions: Business Name i.e., Haddley Locksmiths Logo & colour palette. Branding guidelines, and logos in eps format attached.
What I like: Minimalist, simple, subtle, clean, sophisticated, classic, stylish - examples attached.
Do not include: Website URL or phone number. No additional images to be included.
Coverage: Signage not required on front or roof. Vehicle rear and sides required. Sides can be partially covered i.e., it’s fine if the design only covers a proportion of the sides.
Design Versions: Two versions
1. full colour version
2. mono version - just using the black, white and greys

Target Market(s)

General Public

Industry/Entity Type

Locksmith

Font styles to use
Other font styles liked:
• See Brand Guidelines

Colors

Designer to choose only greyscale colors for use in the design.

Requirements
Must have
• Logo and brand colour palette
Nice to have
• NA
Should not have
• Additional images

```html
<!DOCTYPE html>
<html lang="en">
<head>
<meta charset="utf-8">
<title>Haddley Locksmiths – Vehicle Wrap Versions</title>
<link rel="stylesheet" href="https://fonts.googleapis.com/css2?family=Montserrat:wght@800&display=swap">
<style>
  :root {
    --canvas: #ffffff;
    --wrap-black: #0b0b0b;
    --brand-green: #2f9e45;
    --mid-grey: #6a6a6a;
    --dark-grey: #4a4a4a;
    --soft-grey: #8c8c8c;
    --light-grey: #e2e2e2;
  }
  html, body {
    margin: 0;
    padding: 0;
    width: 1200px;
    height: 1200px;
    overflow: hidden;
    background: var(--canvas);
  }
  .wrap-sheet {
    position: relative;
    width: 1200px;
    height: 1200px;
  }
  .wrap-version {
    position: absolute;
    left: 0;
    width: 1200px;
    height: 540px;
  }
  .wrap-version--colour { top: 40px; }
  .wrap-version--mono { top: 620px; }
  .side-panel { fill: var(--wrap-black); }
  .brand-name {
    font-family: 'Montserrat', sans-serif;
    font-weight: 800;
  }
  .wrap-version--colour .rear-band { fill: var(--brand-green); }
  .wrap-version--colour .rear-circle { fill: var(--mid-grey); }
  .wrap-version--colour .sill-stripe { fill: var(--brand-green); }
  .wrap-version--colour .brand-name { fill: var(--brand-green); }
  .wrap-version--mono .rear-band { fill: var(--dark-grey); }
  .wrap-version--mono .rear-circle { fill: var(--soft-grey); }
  .wrap-version--mono .sill-stripe { fill: var(--dark-grey); }
  .wrap-version--mono .brand-name--top { fill: var(--light-grey); }
  .wrap-version--mono .brand-name--main { fill: var(--mid-grey); }
</style>
</head>
<body>
<main class="wrap-sheet">

  <svg class="wrap-version wrap-version--colour" viewBox="0 0 1200 540" aria-label="Full colour side wrap">
    <defs>
      <clipPath id="panel-clip-colour">
        <rect x="70" y="30" width="1060" height="450" rx="44"/>
      </clipPath>
    </defs>
    <rect class="side-panel" x="70" y="30" width="1060" height="450" rx="44"/>
    <g clip-path="url(#panel-clip-colour)">
      <rect class="rear-band" x="1060" y="30" width="80" height="450"/>
      <path class="rear-band" d="M1130 30 L1130 480 L1010 480 Q1090 360 1100 30 Z"/>
      <circle class="rear-circle" cx="975" cy="235" r="150"/>
      <rect class="sill-stripe" x="330" y="452" width="580" height="22"/>
    </g>
    <text class="brand-name brand-name--top" x="398" y="318" font-size="52" textLength="290" lengthAdjust="spacingAndGlyphs">HADDLEY</text>
    <text class="brand-name brand-name--main" x="374" y="400" font-size="80" textLength="430" lengthAdjust="spacingAndGlyphs">Locksmiths</text>
  </svg>

  <svg class="wrap-version wrap-version--mono" viewBox="0 0 1200 540" aria-label="Mono side wrap">
    <defs>
      <clipPath id="panel-clip-mono">
        <rect x="70" y="30" width="1060" height="450" rx="44"/>
      </clipPath>
    </defs>
    <rect class="side-panel" x="70" y="30" width="1060" height="450" rx="44"/>
    <g clip-path="url(#panel-clip-mono)">
      <rect class="rear-band" x="1060" y="30" width="80" height="450"/>
      <path class="rear-band" d="M1130 30 L1130 480 L1010 480 Q1090 360 1100 30 Z"/>
      <circle class="rear-circle" cx="975" cy="235" r="150"/>
      <rect class="sill-stripe" x="330" y="452" width="580" height="22"/>
    </g>
    <text class="brand-name brand-name--top" x="398" y="318" font-size="52" textLength="290" lengthAdjust="spacingAndGlyphs">HADDLEY</text>
    <text class="brand-name brand-name--main" x="374" y="400" font-size="80" textLength="430" lengthAdjust="spacingAndGlyphs">Locksmiths</text>
  </svg>

</main>
</body>
</html>
```